Corvane Tea range - labels for a range of teas.

Our company name is Corvane Tea Company - based in Melbourne, Australia. We have a current logo project with Draft Plaza.

We offer a range of top quality teas - black, green, white, oolongs, herbals, flavoured teas. From Japan, Assam, Darjeeling, Ceylon, Africa and elsewhere. The very best loose teas, and some pyramid tea bags too.

We cover some blends : English Breakfast, African Breakfast, Ceylon Breakfast, Earl Grey amongst them.

And herbal variants: lemon grass and ginger, chamomile, peppermint, rooibos and chilli.

And fruit teas.... and flavoured teas like vanilla, peach and raspberry.

We aim to occupy a modern, contemporary, sophisticated and global space.... but we can be funky too, especially with the fruit and herbal offers. Quality is paramount ! We do not aim to have the biggest range of teas, but we are very particular. And we source directly from origin.... fresh quality teas.

Would lean towards black teas being on a black background label, green teas on a green background, white etas on a white background, herbals maybe on a straw or suitable background, and flavoured teas on a specific background colour too....maybe fuschia? Violet ? But colourful is key.

The panel should indicate teas being Loose or Pyramid bags. And the nett weight should be shown.... Loose could be for example 75 gr, 125 gr 250 gr etc.. And pyramids would show the number of pyramids and weight, example 20 x Pyramids 50 gr
50 Pyramids 150 gr etc.

And 'Corvane Teas' or 'Corvane Tea Company' should be on the panel too. Melbourne can appear as well if it gels with the total look.

There will need to be 2 lines - in order or juxtaposed, doesn't matter - showing the origin and 'mark' and grade. Example being:
Ceylon
Wendrick Pekoe

or

Darjeeling
Morvani TGFOP1

or

China
Jasmine Leaf

We just need templates to cover the different types of tea - black, green, white, herbal, flavoured - as there are too many (and changing) types of tea in the range .

Any questions...please ask...

Thanks

Reason: Needs to have alater deadline than the current Logo Project associated with the same Corvane Tea Company start up.

Target Market(s)

Sophisticated. Real tea lovers. Discriminating tastes.

Weight

Font styles to use
Sans Serif

Requirements
Must have
• Sophisticated
Cool
Premium quality branding
Bold
Uber modern
Nice to have
• BOLD text.....
Cool fonts....
Pretty bold and minimalist - ultra modern if possible....uber modern
Bright colours and use of black and white..... Not really into pastels etc..

Lots of black colour too is a likely plus
Should not have
• Frilly stuff

```html
<!DOCTYPE html>
<html lang="en">
<head>
<meta charset="utf-8">
<title>Corvane Tea — Label Range</title>
<link rel="stylesheet" href="https://fonts.googleapis.com/css2?family=Inter:wght@700;800&display=swap">
<style>
  :root {
    --page: #ffffff;
    --ink-white: #ffffff;
    --rule: #9a9a9a;

    --black-bg: #000000;
    --black-word: #8c8c8c;

    --herbal-bg: #c4b79c;
    --herbal-word: #f7ef00;

    --white-bg: #86878a;
    --white-word: #ececec;

    --green-bg: #29382f;
    --green-word: #8cc63f;

    --flavoured-bg: #9b8679;
    --flavoured-word: #d3df00;

    --oolong-bg: #58585a;
    --oolong-word: #c6b99b;

    --mark-fill: #5b5b5b;
  }

  * { margin: 0; padding: 0; box-sizing: border-box; }

  html, body {
    width: 1200px;
    height: 848px;
    overflow: hidden;
    background: var(--page);
  }

  .range {
    position: relative;
    width: 1200px;
    height: 848px;
    font-family: "Inter", Arial, Helvetica, sans-serif;
  }

  .label {
    position: absolute;
    width: 202px;
    height: 281px;
    overflow: hidden;
    background: var(--bg);
    color: var(--ink-white);
  }

  .label--black     { --bg: var(--black-bg);     --word: var(--black-word);     left: 49px;  top: 40px; }
  .label--herbal    { --bg: var(--herbal-bg);    --word: var(--herbal-word);    left: 308px; top: 40px; }
  .label--white     { --bg: var(--white-bg);     --word: var(--white-word);     left: 570px; top: 40px; }
  .label--green     { --bg: var(--green-bg);     --word: var(--green-word);     left: 823px; top: 40px; }
  .label--flavoured { --bg: var(--flavoured-bg); --word: var(--flavoured-word); left: 49px;  top: 364px; height: 286px; }
  .label--oolong    { --bg: var(--oolong-bg);    --word: var(--oolong-word);    left: 311px; top: 363px; height: 281px; }

  .label__type {
    position: absolute;
    left: -4px;
    top: 0;
    writing-mode: vertical-rl;
    transform: rotate(180deg);
    font-size: 66px;
    font-weight: 800;
    line-height: 0.82;
    letter-spacing: -0.05em;
    color: var(--word);
    white-space: nowrap;
  }

  .label__tea {
    position: absolute;
    right: 2px;
    top: -2px;
    font-size: 66px;
    font-weight: 800;
    line-height: 1;
    letter-spacing: -0.04em;
    color: var(--ink-white);
  }

  .label__rule {
    position: absolute;
    left: 54px;
    right: 2px;
    top: 75px;
    height: 1px;
    background: var(--rule);
  }

  .label__origin {
    position: absolute;
    left: 56px;
    top: 89px;
    font-size: 26px;
    font-weight: 700;
    letter-spacing: -0.03em;
    color: var(--word);
    white-space: nowrap;
  }

  .label__grade {
    position: absolute;
    left: 57px;
    top: 130px;
    font-size: 15px;
    font-weight: 700;
    letter-spacing: -0.02em;
    color: var(--word);
  }

  .label__brand {
    position: absolute;
    left: 0;
    right: 0;
    bottom: 58px;
    display: flex;
    align-items: center;
    justify-content: center;
    gap: 7px;
    padding-left: 22px;
  }

  .label__brand-box {
    width: 22px;
    height: 22px;
    border: 1px solid var(--ink-white);
    background: var(--mark-fill);
  }

  .label__brand-name {
    font-size: 13px;
    font-weight: 700;
    letter-spacing: -0.01em;
    color: var(--ink-white);
    white-space: nowrap;
  }

  .label__weight {
    position: absolute;
    left: 0;
    right: 0;
    padding-left: 22px;
    bottom: 22px;
    text-align: center;
    font-size: 19px;
    font-weight: 700;
    letter-spacing: -0.02em;
    color: var(--ink-white);
  }
</style>
</head>
<body>
<main class="range">

  <section class="label label--black">
    <span class="label__type">Black</span>
    <span class="label__tea">TEA</span>
    <span class="label__rule"></span>
    <span class="label__origin">Darjeeling</span>
    <span class="label__grade">Morvani TGFOP1</span>
    <div class="label__brand"><span class="label__brand-box"></span><span class="label__brand-name">Corvane Tea</span></div>
    <span class="label__weight">125g</span>
  </section>

  <section class="label label--herbal">
    <span class="label__type">Herbal</span>
    <span class="label__tea">TEA</span>
    <span class="label__rule" style="background: var(--herbal-word);"></span>
    <span class="label__origin" style="font-size:22px; top:93px;">Chamomile</span>
    <div class="label__brand"><span class="label__brand-box"></span><span class="label__brand-name">Corvane Tea</span></div>
    <span class="label__weight">125g</span>
  </section>

  <section class="label label--white">
    <span class="label__type">White</span>
    <span class="label__tea">TEA</span>
    <span class="label__rule" style="background: var(--white-word);"></span>
    <div class="label__brand"><span class="label__brand-box"></span><span class="label__brand-name">Corvane Tea</span></div>
    <span class="label__weight">125g</span>
  </section>

  <section class="label label--green">
    <span class="label__type">Green</span>
    <span class="label__tea">TEA</span>
    <span class="label__rule"></span>
    <div class="label__brand"><span class="label__brand-box"></span><span class="label__brand-name">Corvane Tea</span></div>
    <span class="label__weight">125g</span>
  </section>

  <section class="label label--flavoured">
    <span class="label__type" style="letter-spacing:-0.06em;">Flavoured</span>
    <span class="label__tea">TEA</span>
    <span class="label__rule" style="background: #c9c0b8;"></span>
    <div class="label__brand"><span class="label__brand-box"></span><span class="label__brand-name">Corvane Tea</span></div>
    <span class="label__weight">125g</span>
  </section>

  <section class="label label--oolong">
    <span class="label__type" style="top:10px;">Oolong</span>
    <span class="label__tea">TEA</span>
    <span class="label__rule"></span>
    <div class="label__brand"><span class="label__brand-box"></span><span class="label__brand-name">Corvane Tea</span></div>
    <span class="label__weight">125g</span>
  </section>

</main>
</body>
</html>
```